Business Card Design Project

Beauty Therapist
Bold, bright, feminine, like contrast, love flowers, girly stuff. Must be beautiful. But open to all suggestions. Business name: Plucky Plum.
xxx
Dorota Kaczmarczyk
Updates

Project Deadline Extended
Reason: I think you need more time to design something good. X

Target Market(s)

ignore this

Industry/Entity Type

Business

```html
<!DOCTYPE html>
<html lang="en">
<head>
<meta charset="utf-8">
<title>Plucky Plum – Business Card</title>
<link rel="stylesheet" href="https://fonts.googleapis.com/css2?family=Dancing+Script:wght@400;500&family=Quicksand:wght@400&display=swap">
<style>
  :root {
    --stage: #4a4a4a;
    --cream-light: #fffdf6;
    --cream-mid: #fdf0d8;
    --cream-warm: #f9dfb4;
    --berry-red: #e3202a;
    --ink: #1d1d1d;
    --warm-coral: #f26a4a;
    --warm-orange: #f6a04a;
  }
  * { box-sizing: border-box; margin: 0; padding: 0; }
  html, body {
    width: 1027px; height: 1200px; overflow: hidden;
    background: var(--stage);
  }
  .canvas { position: relative; width: 1027px; height: 1200px; }

  .card {
    position: absolute; left: 33px; width: 960px; height: 554px;
    overflow: hidden;
    background:
      radial-gradient(ellipse at 20% 15%, var(--cream-light) 0%, transparent 60%),
      linear-gradient(160deg, var(--cream-light) 0%, var(--cream-mid) 55%, var(--cream-warm) 100%);
    box-shadow: 0 4px 10px rgba(0,0,0,.45);
  }
  .card--front { top: 28px; }
  .card--back  { top: 611px; }

  .illustration { position: absolute; }
  .illustration--front {
    right: 0; bottom: 0; width: 720px; height: 330px;
    background: radial-gradient(ellipse at 100% 100%, var(--warm-coral) 0%, var(--warm-orange) 35%, rgba(249,223,180,0.6) 65%, rgba(249,223,180,0) 100%);
  }
  .illustration--back {
    left: 0; bottom: 0; width: 640px; height: 300px;
    background: radial-gradient(ellipse at 0% 100%, var(--warm-orange) 0%, var(--warm-coral) 35%, rgba(249,223,180,0.6) 65%, rgba(249,223,180,0) 100%);
  }

  .script {
    position: absolute; color: var(--berry-red); white-space: nowrap; line-height: 1;
    font-family: "Dancing Script", cursive;
  }
  .caps {
    position: absolute; color: var(--ink); white-space: nowrap; line-height: 1;
    font-family: "Quicksand", sans-serif; font-weight: 400; text-transform: uppercase;
  }

  .front-brand {
    left: 132px; top: 112px; font-weight: 500; font-size: 168px;
    text-shadow: 0 0 2px #fff, 0 0 2px #fff;
  }
  .front-role { left: 107px; top: 330px; font-size: 70px; letter-spacing: 4px; }

  .back-name { right: 54px; top: 70px; font-weight: 400; font-size: 80px; }
  .back-role { right: 56px; top: 180px; font-size: 40px; letter-spacing: 3px; }
  .back-phone { right: 56px; top: 243px; font-weight: 400; font-size: 56px; letter-spacing: 1px; }
  .back-brand { right: 56px; top: 404px; font-weight: 500; font-size: 80px; }
</style>
</head>
<body>
<div class="canvas">

  <section class="card card--front">
    <div class="illustration illustration--front" role="img" aria-label="Placeholder for a floral illustration of red, orange and yellow petals with green leaves"></div>
    <div class="script front-brand">Plucky Plum</div>
    <div class="caps front-role">Beauty Therapist</div>
  </section>

  <section class="card card--back">
    <div class="illustration illustration--back" role="img" aria-label="Placeholder for a floral illustration of red, orange and yellow petals with green leaves"></div>
    <div class="script back-name">Dorota Kaczmarczyk</div>
    <div class="caps back-role">Beauty Therapist</div>
    <div class="script back-phone">020 9876 5432</div>
    <div class="script back-brand">Plucky Plum</div>
  </section>

</div>
</body>
</html>
```